Corporate consulting business needs a business card

I want a professional business card.... surprise me

Updates

Reason: i dont think 2 days is enough

Target Market(s)

Corprorate and Not for Profit firms and organisations

Industry/Entity Type

Consulting

Contact Information for Business Card

Logo
Corporate Consulting Services
On Time, On Budget, Beyond Expectation
Tovan Presfield
Director
0427 31 94 62 (Larger)
tovan@tp-advisory.com.au
www.tp-advisory.com.au
include little icons beside the contact info:

- Envelope = email
- Phone = phone
- Globe = website

Font styles to use
Serif
Sans Serif

Requirements
Must have
• Professional and clean
Nice to have
• you tell me

```html
<!DOCTYPE html>
<html lang="en">
<head>
<meta charset="utf-8">
<title>TP Advisory – Business Card</title>
<link href="https://fonts.googleapis.com/css2?family=Libre+Baskerville:wght@400;700&family=Open+Sans:wght@400;600;700&display=swap" rel="stylesheet">
<style>
  :root {
    --backdrop: #5f5f5f;
    --card: #ffffff;
    --brand-brown: #5a3a24;
    --name-brown: #4e3120;
    --text-grey: #6b6b6b;
    --text-dark: #3a3a3a;
    --serif: "Libre Baskerville", Georgia, serif;
    --sans: "Open Sans", Arial, sans-serif;
  }
  * { box-sizing: border-box; margin: 0; padding: 0; }
  html, body { width: 1200px; height: 843px; overflow: hidden; }
  body {
    background: var(--backdrop);
    display: flex;
    flex-direction: column;
    align-items: center;
    justify-content: center;
    gap: 36px;
  }
  .card {
    position: relative;
    width: 640px;
    height: 366px;
    background: var(--card);
    border-radius: 22px;
    overflow: hidden;
    box-shadow: 0 6px 18px rgba(0,0,0,0.35);
  }

  /* Back side */
  .card-back {
    display: flex;
    flex-direction: column;
    align-items: center;
    justify-content: center;
    text-align: center;
  }
  .brand-lockup {
    display: flex;
    align-items: center;
    gap: 14px;
    margin-bottom: 30px;
  }
  .brand-dot {
    width: 46px; height: 46px;
    border: 2px solid var(--brand-brown);
    border-radius: 50%;
  }
  .brand-name {
    font-family: var(--serif);
    font-weight: 700;
    font-size: 30px;
    color: var(--brand-brown);
    letter-spacing: 1px;
  }
  .tagline {
    font-family: var(--sans);
    font-size: 17px;
    color: var(--text-grey);
    line-height: 1.45;
  }

  /* Front side */
  .card-front .edge-tab {
    position: absolute;
    left: -22px; top: 96px;
    width: 44px; height: 44px;
    border-radius: 50%;
    background: var(--brand-brown);
  }
  .person {
    position: absolute;
    left: 42px; top: 98px;
  }
  .person-name {
    font-family: var(--sans);
    font-weight: 700;
    font-size: 24px;
    color: var(--name-brown);
  }
  .person-role {
    font-family: var(--sans);
    font-size: 15px;
    color: var(--text-dark);
    margin-top: -2px;
  }
  .contact-list {
    position: absolute;
    left: 34px; top: 168px;
    list-style: none;
    font-family: var(--sans);
    color: var(--text-grey);
  }
  .contact-list li {
    display: flex;
    align-items: center;
    gap: 10px;
    margin-bottom: 6px;
    font-size: 16px;
  }
  .contact-list li.phone { font-size: 25px; margin-bottom: 8px; }
  .contact-list svg { width: 14px; height: 14px; fill: var(--text-dark); flex: none; }
  .brand-mark {
    position: absolute;
    right: 34px; top: 58px;
    width: 250px; height: 250px;
    border: 4px solid var(--brand-brown);
    border-radius: 50%;
    display: flex;
    align-items: center;
    justify-content: center;
  }
  .brand-mark .brand-name { font-size: 34px; }
</style>
</head>
<body>
  <section class="card card-back" aria-label="Card back">
    <div class="brand-lockup">
      <span class="brand-dot"></span>
      <span class="brand-name">TP Advisory</span>
    </div>
    <p class="tagline">Corporate Consulting Services<br>On Time, On Budget, Beyond Expectation</p>
  </section>

  <section class="card card-front" aria-label="Card front">
    <span class="edge-tab"></span>
    <div class="person">
      <h1 class="person-name">Tovan Presfield</h1>
      <p class="person-role">Director</p>
    </div>
    <ul class="contact-list">
      <li class="phone">
        <svg viewBox="0 0 24 24" aria-hidden="true"><path d="M6.6 10.8a15.1 15.1 0 0 0 6.6 6.6l2.2-2.2c.3-.3.7-.4 1-.2 1.1.4 2.3.6 3.6.6.6 0 1 .4 1 1V20c0 .6-.4 1-1 1A17 17 0 0 1 3 4c0-.6.4-1 1-1h3.5c.6 0 1 .4 1 1 0 1.3.2 2.5.6 3.6.1.3 0 .7-.2 1z"/></svg>
        0427 31 94 62
      </li>
      <li class="email">
        <svg viewBox="0 0 24 24" aria-hidden="true"><path d="M2 5h20v14H2zm2 2v.5l8 5 8-5V7zm0 2.8V17h16V9.8l-8 5z"/></svg>
        tovan@tp-advisory.com.au
      </li>
      <li class="web">
        <svg viewBox="0 0 24 24" aria-hidden="true"><path d="M12 2a10 10 0 1 0 0 20 10 10 0 0 0 0-20zm6.9 6h-3a15 15 0 0 0-1.3-3.9A8 8 0 0 1 18.9 8zM12 4c.8 1.2 1.5 2.5 1.9 4h-3.8c.4-1.5 1.1-2.8 1.9-4zM4.3 14a8 8 0 0 1 0-4h3.3a16 16 0 0 0 0 4zm.8 2h3a15 15 0 0 0 1.3 3.9A8 8 0 0 1 5.1 16zm3-8h-3a8 8 0 0 1 4.3-3.9C8.8 5.3 8.4 6.6 8.1 8zM12 20c-.8-1.2-1.5-2.5-1.9-4h3.8c-.4 1.5-1.1 2.8-1.9 4zm2.3-6H9.7a14 14 0 0 1 0-4h4.6a14 14 0 0 1 0 4zm.3 5.9c.6-1.2 1-2.5 1.3-3.9h3a8 8 0 0 1-4.3 3.9zm1.8-5.9a16 16 0 0 0 0-4h3.3a8 8 0 0 1 0 4z"/></svg>
        www.tp-advisory.com.au
      </li>
    </ul>
    <div class="brand-mark">
      <span class="brand-name">TP Advisory</span>
    </div>
  </section>
</body>
</html>
```